Law firm website marketed direct to many individual clients

I need someone to design a very basic website for a law firm that will be very eye catching. It's going to be a single-paged, scrolling website with a small number of folds. I have uploaded a simple word document that outlines the basics of what I thought could be the layout, but I am open to suggestion on font, size, shades of color, organization, etc. etc. Essentially the website just needs to be a very efficient and visually appealing way of conveying some simple messages.

Target Market(s)

High volumes of individuals who have gotten into a car accident and then google on their phones a lawyer to hire to represent them.

Industry/Entity Type

Legal

Number of Pages Required

1 page

Font styles to use
Serif
Sans Serif

Colors
34a7d7
85cae6
0592cd

Requirements
Must have
• Must be bright and grab the users attention with color scheme and layout. The different sections should be done in such a way that they can fit entirely onto one smart phone or tablet screen.
Nice to have
• I'd like to try and see what it looks like if in the middle somewhere there is a fold that says "MEET YOUR ATTORNEYS" and includes individual photos of two attorneys, one on the left side and one on the right. And then a small bio section on them. I don't want the photos to include a square or rectangle background, I want the person in the photo to be superimposed on top of whatever pattern or background you have in the fold.
Should not have
• Do not want too much text. Anything more than 2 sentences in any single place is unacceptable.

```html
<!DOCTYPE html>
<html lang="en">
<head>
<meta charset="utf-8">
<title>Meridian Law Practice</title>
<link rel="stylesheet" href="https://fonts.googleapis.com/css2?family=Lato:wght@300;400;700&family=Raleway:wght@300;400;600&display=swap">
<style>
:root{
  --blue:#3399dd;
  --blue-deep:#0592cd;
  --blue-light:#85cae6;
  --cyan:#34c6d7;
  --red:#e65454;
  --ink:#222;
  --dark:#363636;
  --grey-box:#efefef;
  --grey-line:#9a9a9a;
  --footer:#efefef;
  --map:#a9dcb0;
}
*{margin:0;padding:0;box-sizing:border-box}
html,body{width:1200px;height:4225px;overflow:hidden;background:#fff}
body{position:relative;font-family:'Lato',sans-serif;color:var(--ink)}
.abs{position:absolute}
.center{left:0;width:1200px;text-align:center}

/* hero */
.hero{position:absolute;left:0;top:0;width:1200px;height:670px;
  background:linear-gradient(90deg,#3b3a3c 0%,#6a6466 30%,#4a4b52 55%,#2b2e38 80%,#3e3f46 100%)}
.hero-shade{position:absolute;inset:0;background:rgba(0,0,0,.35)}
.nav-bar{position:absolute;left:0;top:0;width:1200px;height:64px;background:rgba(0,0,0,.25)}
.brand{position:absolute;left:45px;top:8px;color:#fff}
.brand-name{font-family:'Raleway',sans-serif;font-weight:600;font-size:28px;letter-spacing:2px;line-height:32px}
.brand-sub{font-size:8px;letter-spacing:1px;border-top:1px solid #fff;margin-top:2px;padding-top:2px;width:60px}
.nav a{position:absolute;top:20px;color:#fff;text-decoration:none;font-size:14px;font-weight:700;letter-spacing:1px}
.nav a.active{color:#8fd0ee;border-bottom:2px solid #8fd0ee;padding-bottom:6px}
.hero-title{top:236px;font-family:'Raleway',sans-serif;font-weight:600;font-size:72px;letter-spacing:6px;color:#fff}
.hero-sub{top:326px;font-family:'Raleway',sans-serif;font-weight:300;font-size:42px;letter-spacing:6px;color:#e6e6e6}
.btn-red{position:absolute;left:465px;top:478px;width:267px;height:52px;background:var(--red);color:#fff;
  font-size:16px;font-weight:700;letter-spacing:1px;line-height:52px;text-align:center}
.hero-tab{position:absolute;left:552px;top:622px}

/* blue */
.accident{position:absolute;left:0;top:670px;width:1200px;height:536px;background:var(--blue)}
.kicker{top:70px;font-size:28px;color:#fff;letter-spacing:2px}
.case-box{position:absolute;background:rgba(5,146,205,.55);color:#fff;text-align:center;font-weight:300;letter-spacing:5px}
.case-1{left:332px;top:181px;width:533px;height:87px;font-size:76px;line-height:87px}
.case-2{left:392px;top:282px;width:416px;height:68px;font-size:52px;line-height:68px}
.btn-outline{position:absolute;left:465px;top:409px;width:270px;height:59px;border:1px solid #bfe3f6;color:#fff;
  font-size:17px;font-weight:700;letter-spacing:1px;text-align:center;line-height:57px}

/* attorneys */
.attorneys{position:absolute;left:0;top:1206px;width:1200px;height:743px;
  background:linear-gradient(160deg,#f7f7f7 0%,#ececec 45%,#f6f6f6 55%,#ededed 100%)}
.section-title{top:48px;font-size:46px;font-weight:400;letter-spacing:3px;color:var(--blue-deep)}
.title-rule{position:absolute;left:465px;top:115px;width:270px;height:3px;background:var(--blue)}
.portrait{position:absolute;top:174px;border-radius:44% 44% 4px 4px;
  background:linear-gradient(180deg,#c9b8ad 0%,#6e6f75 35%,#23252b 100%)}
.name{position:absolute;top:512px;width:420px;text-align:center;font-size:20px;letter-spacing:1.5px;color:#333}
.name small{font-size:13px;color:#888;letter-spacing:.5px}
.role{position:absolute;top:550px;width:420px;text-align:center;font-size:13px;font-weight:700;letter-spacing:2px;color:var(--cyan)}
.btn-dark{position:absolute;top:608px;width:254px;height:48px;background:var(--dark);color:#fff;
  font-size:14px;font-weight:700;letter-spacing:1px;text-align:center;line-height:48px}

/* features */
.feature{position:absolute;width:516px;height:244px;background:var(--grey-box);text-align:center}
.feature-icon{position:absolute;left:0;top:28px;width:516px;height:50px;display:flex;justify-content:center;align-items:center;font-size:20px;letter-spacing:2px}
.feature-label{position:absolute;left:83px;top:92px;width:350px;height:36px;border:3px solid #aaa;background:#fff;
  font-size:14px;letter-spacing:1.5px;line-height:30px;color:#333}
.feature-text{position:absolute;left:0;top:152px;width:516px;font-size:14px;color:#333}
.feature-more{position:absolute;left:0;top:200px;width:516px;font-size:12px;color:#999}

/* dark */
.promise{position:absolute;left:0;top:2648px;width:1200px;height:687px;background:var(--dark);color:#fff}
.promise h2{position:absolute;left:0;width:1200px;text-align:center;font-weight:300;font-size:54px;letter-spacing:5px}
.promise p{position:absolute;left:0;width:1200px;text-align:center;font-size:19px;letter-spacing:1.5px;line-height:48px}

/* contact */
.map{position:absolute;left:45px;top:3403px;width:1107px;height:451px;
  background:linear-gradient(135deg,#b8e3bc 0%,#9fd6a6 45%,#b4e0b7 70%,#a2d8a8 100%)}
.card{position:absolute;left:203px;top:3713px;width:794px;height:200px;background:#fff;padding:44px 55px}
.card-kicker{font-size:11px;color:#4aa58a;letter-spacing:1px}
.card-title{font-size:38px;font-weight:300;letter-spacing:2px;margin-top:12px;color:#222}
.card-text{font-size:15px;line-height:26px;margin-top:6px;color:#444;width:420px}
.info-col{position:absolute;top:3922px;width:300px;text-align:center}
.info-head{font-size:12px;font-weight:700;letter-spacing:1px;color:#222}
.info-line{font-size:14px;color:#999;line-height:24px;margin-top:16px}

/* footer */
.footer{position:absolute;left:0;top:4062px;width:1200px;height:163px;background:var(--footer)}
.footer-text{top:78px;font-size:13px;color:#999;letter-spacing:.5px}
.to-top{position:absolute;left:1078px;top:58px;width:54px;height:54px;border-radius:50%;background:#e2e2e2;border:1px solid #d4d4d4}
</style>
</head>
<body>

<header class="hero">
  <div class="abs" role="img" aria-label="Photo of three lawyers meeting at a desk with a laptop" style="inset:0"></div>
  <div class="hero-shade"></div>
  <div class="nav-bar"></div>
  <div class="brand">
    <div class="brand-name">MERIDIAN</div>
    <div class="brand-sub">LAW GROUP</div>
  </div>
  <nav class="nav">
    <a class="active" style="left:734px">HOME</a>
    <a style="left:832px">ABOUT US</a>
    <a style="left:965px">CONTACT</a>
    <a style="left:1093px">FILLER</a>
  </nav>
  <div class="abs center hero-title">MERIDIAN</div>
  <div class="abs center hero-sub">LAW PRACTICE</div>
  <div class="btn-red">KNOW US BETTER</div>
  <svg class="hero-tab" width="96" height="48" viewBox="0 0 96 48">
    <polygon points="0,48 48,0 96,48" fill="#fff"/>
    <path d="M42 30 L48 36 L54 30 M48 24 V36" stroke="#888" stroke-width="2" fill="none"/>
  </svg>
</header>

<section class="accident">
  <div class="abs center kicker">ACCIDENT? &nbsp;INJURED?</div>
  <div class="case-box case-1">YOUR CASE</div>
  <div class="case-box case-2">YOUR MONEY</div>
  <div class="btn-outline">LEARN MORE</div>
</section>

<section class="attorneys">
  <h2 class="abs center section-title">MEET YOUR ATTORNEYS</h2>
  <div class="title-rule"></div>

  <div class="portrait" role="img" aria-label="Portrait of senior partner Daniel Hartley in a dark suit" style="left:192px;width:219px;height:276px"></div>
  <div class="name" style="left:90px">Daniel Hartley,<small>LLB TEP</small></div>
  <div class="role" style="left:90px">SENIOR PARTNER</div>
  <div class="btn-dark" style="left:163px">SEND DANIEL A MESSAGE</div>

  <div class="portrait" role="img" aria-label="Portrait of junior partner Owen Castell in a dark suit" style="left:778px;width:242px;height:276px"></div>
  <div class="name" style="left:694px">Owen Castell,<small>LLB MSSc</small></div>
  <div class="role" style="left:694px">JUNIOR PARTNER</div>
  <div class="btn-dark" style="left:778px">SEND OWEN A MESSAGE</div>
</section>

<section class="features">
  <div class="feature" style="left:45px;top:2045px">
    <div class="feature-icon" style="font-size:40px">$</div>
    <div class="feature-label">LOW FEES</div>
    <div class="feature-text">We charge less, so you keep more.</div>
    <div class="feature-more">learn more -&gt;</div>
  </div>
  <div class="feature" style="left:638px;top:2045px">
    <div class="feature-icon">FREE</div>
    <div class="feature-label">FREE CONSULTATION</div>
    <div class="feature-text">It's always free to talk to us.</div>
    <div class="feature-more">learn more -&gt;</div>
  </div>
  <div class="feature" style="left:45px;top:2321px">
    <div class="feature-icon">
      <svg width="28" height="50" viewBox="0 0 28 50"><rect x="2" y="2" width="24" height="46" rx="4" fill="none" stroke="#333" stroke-width="2"/><line x1="2" y1="40" x2="26" y2="40" stroke="#333" stroke-width="2"/></svg>
    </div>
    <div class="feature-label">GET STARTED WITH YOUR PHONE</div>
    <div class="feature-text">No need to come to the office, sign up using your phone.</div>
    <div class="feature-more">learn more -&gt;</div>
  </div>
  <div class="feature" style="left:638px;top:2321px">
    <div class="feature-icon">
      <svg width="110" height="44" viewBox="0 0 110 44">
        <circle cx="20" cy="22" r="18" fill="none" stroke="#333" stroke-width="2"/>
        <circle cx="20" cy="17" r="6" fill="#333"/><path d="M9 33 Q20 22 31 33" fill="#333"/>
        <line x1="40" y1="22" x2="70" y2="22" stroke="#333" stroke-width="2"/>
        <circle cx="90" cy="22" r="18" fill="none" stroke="#333" stroke-width="2"/>
        <circle cx="90" cy="17" r="6" fill="#333"/><path d="M79 33 Q90 22 101 33" fill="#333"/>
      </svg>
    </div>
    <div class="feature-label">SPEAK DIRECTLY TO A LAWYER</div>
    <div class="feature-text">No staff screening. Talk right to a lawyer on your first call.</div>
    <div class="feature-more">learn more -&gt;</div>
  </div>
</section>

<section class="promise">
  <h2 style="top:118px">NO FEE UNLESS WE WIN</h2>
  <p style="top:210px">We don't get paid unless you get paid.<br>It's as simple as that. We let our results do the talking for us.</p>
  <h2 style="top:376px">QUESTIONS ABOUT ANYTHING?</h2>
  <p style="top:468px;font-size:18px">We're here to help. Feel free to call us at 555-014-2290 to speak to one of our attorneys. With extensive<br>experience in helping clients get the results that they want, our team is always just a phone call away.</p>
</section>

<section class="contact">
  <div class="map" role="img" aria-label="Map of the office area with roads and a lake"></div>
  <div class="card">
    <div class="card-kicker">GET IN TOUCH</div>
    <div class="card-title">CONTACT INFO</div>
    <div class="card-text">Lorem ipsum dolor sit amet, consectetur adipisc elit. Nullam vehicula arcu at.</div>
  </div>
  <div class="info-col" style="left:295px">
    <div class="info-head">CONTACT US</div>
    <div class="info-line">T. 555-014-2290<br>hello@meridianlaw.com</div>
  </div>
  <div class="info-col" style="left:625px">
    <div class="info-head">RIVERTON</div>
    <div class="info-line">ST 40211<br>Main Office Downtown</div>
  </div>
</section>

<footer class="footer">
  <div class="abs center footer-text">MERIDIAN LAW GROUP© 2016 All Right Reserved</div>
  <div class="to-top">
    <svg width="54" height="54" viewBox="0 0 54 54"><path d="M18 31 L27 22 L36 31" stroke="#999" stroke-width="2" fill="none"/></svg>
  </div>
</footer>

</body>
</html>
```